A Dedicated Thank You to my Dad

Proposed Dimensions: Approx. 20" x 30"

For Father's Day, I wrote a dedication to my Dad that encapsulates my gratitude for everything he does, and everything he is. His birthday is on August 3, but it is more important for me to transform this dedication into a meaningful and memorable gift than to meet any deadline. I would love an image that captures the relationship between a father and his son, accompanied by my words of thanks in some sort of font that is appropriate for the message (calligprahy? not sure about that).

I had actually posted the Thank You on Pixelmarrow as a public post, so anyone with an account can read it: https://www.pixelmarrow.example/photo.php?fbid=40872219360548813&set=a.318760942157.6650129.3908471&type=1&theater

Only the words starting with "Thank you ..." should be on the poster.

Target Market(s)

This is a personal gift for my Dad. He doesn't have the best of eyesight, so having the words in a really small font would not be particularly helpful. :-)

Requirements
Must have
• * Personable
* Warm
* Inviting
* Memorable
* Understated more favored over Loud
Should not have
• * An entire palette of colors
* Wacky colors or fonts

```html
<!DOCTYPE html>
<html lang="en">
<head>
<meta charset="utf-8">
<title>Thank You, Dad</title>
<link rel="stylesheet" href="https://fonts.googleapis.com/css2?family=Cinzel:wght@700&family=Arimo:wght@700&family=Kaushan+Script&display=swap">
<style>
  :root {
    --backdrop: #ececec;
    --paper: #fbfbfa;
    --ink: #3a1a12;
    --ember: #d9711b;
    --sun-top: #f2a22a;
    --sun-mid: #c9651a;
    --sea-dark: #2a1008;
    --shadow: rgba(0,0,0,0.35);
  }
  * { margin: 0; padding: 0; box-sizing: border-box; }
  html, body {
    width: 923px; height: 1200px; overflow: hidden;
    background: var(--backdrop);
  }
  .poster {
    position: absolute;
    left: 51px; top: 26px;
    width: 820px; height: 1148px;
    background: var(--paper);
    box-shadow: -14px 18px 30px var(--shadow);
    overflow: hidden;
  }
  .hero-photo {
    position: absolute; left: 0; top: 0;
    width: 820px; height: 474px;
    background:
      radial-gradient(ellipse 160px 60px at 320px 100px, #ffe79a 0%, rgba(255,210,90,0.6) 40%, rgba(255,180,60,0) 100%),
      linear-gradient(180deg, #5a2a12 0%, var(--sun-top) 16%, #e88a24 28%, var(--sun-mid) 42%, #b85a18 62%, #6b2c10 82%, var(--sea-dark) 100%);
  }
  .hero-photo .shore {
    position: absolute; right: 0; top: 130px;
    width: 420px; height: 344px;
    background: linear-gradient(160deg, rgba(30,10,5,0) 0%, rgba(30,10,5,0.85) 35%, #1e0a05 100%);
  }
  .headline {
    position: absolute; left: 48px; top: 430px;
    font-family: 'Arimo', sans-serif; font-weight: 700;
    font-size: 76px; letter-spacing: -2px; line-height: 1;
    color: var(--ink);
    -webkit-text-stroke: 1px rgba(255,255,255,0.55);
  }
  .headline-for {
    position: absolute; left: 245px; top: 504px;
    font-family: 'Kaushan Script', cursive;
    font-size: 40px; color: var(--ember);
    transform: rotate(-8deg);
  }
  .gratitude-list {
    position: absolute; left: 58px; top: 578px;
    width: 704px;
    font-family: 'Cinzel', serif; font-weight: 700;
    font-size: 13.6px; line-height: 23.4px;
    text-align: center; color: var(--ink);
  }
  .gratitude-list .warm { color: var(--ember); }
  .closing-line {
    position: absolute; left: 0; top: 1014px; width: 820px;
    text-align: center;
    font-family: 'Kaushan Script', cursive;
    font-size: 21px; color: var(--ember);
    word-spacing: 3px;
  }
</style>
</head>
<body>
  <main class="poster">
    <div class="hero-photo" role="img" aria-label="Beach at sunset with a father and young son walking hand in hand in silhouette along the shoreline">
      <div class="shore"></div>
    </div>

    <h1 class="headline">Thank you</h1>
    <div class="headline-for">for</div>

    <p class="gratitude-list">
      Always carrying us to the car after we fell asleep, even <span class="warm">after</span> we were definitely old <span class="warm">enough to walk it</span> • welcoming <span class="warm">more people to stay with us</span> than I <span class="warm">can count</span> • doggedly trying to teach me that the beach is not to be feared <span class="warm">nor cleaned</span> • loading us all up in <span class="warm">the station wagon,</span> pillows in tow, so we could watch the first <span class="warm">drive-in movie</span> together and squint in the <span class="warm">second</span> • as coach, letting me take a <span class="warm">fake rabbit’s foot</span> onto the <span class="warm">soccer field</span> • letting me sing in my room as <span class="warm">if I were the originating artist</span> • making car trips with you, <span class="warm">wherever</span> we were going, fun and special • putting up with the commutes you did, for decades, so we could grow up amongst <span class="warm">family and friends</span> • my dry sense of humor. I cherish it • <span class="warm">finding</span> a way, by hook or by crook, to send <span class="warm">three children</span> to college at the same <span class="warm">time</span> • never giving up on trying to <span class="warm">convince me that imperfection</span> is not a <span class="warm">failure</span> • teaching me to <span class="warm">try</span> to find the good in everyone • <span class="warm">showing me</span> that there is peace to be <span class="warm">found in stillness and quiet</span> • <span class="warm">demonstrating</span> the fun that can be had and the truths that can be gleaned from debate • accepting me for who I am, no matter who I love, and for helping me to <span class="warm">accept myself</span> • doing whatever you can to <span class="warm">help</span> whoever you can, whether <span class="warm">friend, family or stranger</span> • trusting me enough <span class="warm">to let</span> your guard down to let me know how <span class="warm">you are truly doing</span> • insisting, year <span class="warm">after year,</span> that time with you means <span class="warm">more</span> than <span class="warm">any gift</span> I could ever purchase
    </p>

    <p class="closing-line">That is one lesson, amongst so many, that I will pass down to our next generation.</p>
  </main>
</body>
</html>
```